International Business Consulting Company Website

RV Crestline Advisory is a U.S-based international consulting firm. We combined passion for success in the global business arena with hands-on experience to help foreign companies navigate the entry into U.S. markets and U.S. companies in initiating and expanding exports to foreign markets.

We need a simple 1 page website
Examples of other consultants’ websites:
http://www.falconridgeadvisors.example/#intro
https://www.mtq-advisers.example
http://veronagroup.example
https://harborwiseadvisory.example

I also need the designer to suggest stock images that are suitable (related to international business, exports).

We want our web design to be bold, yet clean and simple.

Target Market(s)

US companies that export abroad, foreign companies that want to do business int he US/ open a subsidiary in the US.

Industry/Entity Type

Business Consultant

Coding

Coded - Design and coding required

Font styles to use
Sans Serif

Requirements
Must have
• Company logo on top

```html
<!DOCTYPE html>
<html lang="en">
<head>
<meta charset="utf-8">
<title>RV Crestline Advisory</title>
<link href="https://fonts.googleapis.com/css2?family=Montserrat:wght@400;600;700;800&family=Open+Sans:wght@400;600;700&display=swap" rel="stylesheet">
<style>
:root{
  --blue:#1f4fa8;
  --blue-deep:#173d86;
  --blue-bright:#2a63c7;
  --ink:#2b2b2b;
  --muted:#555;
  --grey-band:#e6e7e9;
  --rule:#c9ccd2;
  --white:#fff;
}
*{box-sizing:border-box;margin:0;padding:0}
html,body{width:1200px;height:3593px;overflow:hidden;background:#fff}
body{font-family:"Open Sans",Arial,sans-serif;color:var(--ink);position:relative}
.section{position:absolute;left:0;width:1200px}
.btn{display:inline-block;background:linear-gradient(#2c65c9,#173d86);color:#fff;font:700 15px "Open Sans",sans-serif;text-transform:uppercase;padding:9px 26px;border-radius:4px;letter-spacing:.3px;border:1px solid #0f2e6a}

/* header / hero */
.hero{top:0;height:600px;overflow:hidden}
.hero-photo{position:absolute;inset:0;background:linear-gradient(160deg,#8fa7b6 0%,#5b7585 30%,#a47c4e 50%,#3d5f7a 70%,#2b4e6d 100%)}
.brand{position:absolute;left:44px;top:24px;width:320px;height:108px;background:var(--blue);display:flex;align-items:center;padding-left:26px;gap:14px}
.brand-square{width:58px;height:58px;border:3px solid #fff;flex:none}
.brand-name{color:#fff;font:700 26px/1.05 "Open Sans",sans-serif;text-transform:uppercase}
.topbar{position:absolute;right:44px;top:22px;display:flex;gap:22px;align-items:center;color:#fff;font:600 15px "Open Sans",sans-serif}
.topbar span{display:flex;align-items:center;gap:7px}
.social{display:flex;gap:6px}
.social i{width:24px;height:24px;border:2px solid #fff;border-radius:50%;display:block}
.nav{position:absolute;right:40px;top:100px;display:flex;gap:34px;color:#fff;font:700 15px "Open Sans",sans-serif;text-transform:uppercase}
.nav a{color:#fff;text-decoration:none;padding-bottom:6px}
.nav a.active{border-bottom:3px solid #fff}
.arrow{position:absolute;top:370px;width:44px;height:44px;background:var(--blue);display:flex;align-items:center;justify-content:center}
.hero-edge{position:absolute;left:0;bottom:0}

.tagline{top:600px;height:250px;background:var(--grey-band)}
.tagline h1{position:absolute;left:70px;top:98px;width:400px;font:800 24px/1.2 Montserrat,sans-serif;color:#222;text-transform:uppercase;white-space:nowrap}
.tagline h1 em{font-style:normal;color:var(--blue);display:block;font-size:19px;line-height:1.35}
.tagline h1 strong{display:block;font-size:34px;line-height:1.15;color:#222}
.tagline p{position:absolute;left:492px;top:98px;width:640px;font:700 15px/1.55 "Open Sans",sans-serif;color:#333}
.tagline .btn{position:absolute;left:492px;top:172px;font-size:13px;padding:7px 24px}

.sec-title{display:flex;justify-content:center;align-items:center;gap:14px;font:400 28px Montserrat,sans-serif;text-transform:uppercase}
.sec-title .mark{width:46px;height:46px;border:3px solid currentColor}
.sec-title span{border-bottom:3px solid var(--rule);padding:4px 2px 8px}
.sec-title b{color:var(--blue);font-weight:700}
.dark .sec-title{color:#fff}
.dark .sec-title b{color:#fff}

.about{top:850px;height:527px}
.about .sec-title{position:absolute;top:60px;left:0;right:0}
.about-lead{position:absolute;left:52px;top:140px;width:250px;font:400 18px/1.4 "Open Sans",sans-serif;color:#333}
.about-body{position:absolute;left:340px;top:140px;width:600px;font:400 13.5px/1.6 "Open Sans",sans-serif;color:#444}
.about-body p+p{margin-top:18px}
.about-body .btn{margin-top:18px}
.portrait{position:absolute;left:990px;top:145px;width:152px;height:152px;border-radius:50%;background:radial-gradient(circle at 50% 40%,#6c5446,#2a1d18);border:4px solid #ddd}

.dark{color:#fff;overflow:hidden}
.dark-photo{position:absolute;inset:0}
.dark-edge{position:absolute;left:0}
.exports{top:1377px;height:563px}
.exports .dark-photo{background:linear-gradient(180deg,#3a3f4d 0%,#5a4c44 45%,#6b4a35 70%,#3b3432 100%)}
.exports .sec-title{position:absolute;top:110px;left:0;right:0}
.lead{font:700 17px "Open Sans",sans-serif;text-align:center}
.exports .lead{position:absolute;top:200px;left:0;right:0}
.feature-grid{position:absolute;display:grid;row-gap:20px}
.exports .feature-grid{left:110px;top:260px;width:1000px;grid-template-columns:500px 500px}
.feature{display:flex;gap:18px;align-items:center;font:700 13.5px/1.4 "Open Sans",sans-serif;white-space:nowrap}
.icon{width:52px;height:52px;flex:none;display:flex;align-items:center;justify-content:center}
.exports .icon{background:#fff}
.fdi .icon{background:var(--blue)}

.fdi{top:1940px;height:503px}
.fdi .sec-title{position:absolute;top:80px;left:0;right:0;color:#333}
.fdi .lead{position:absolute;top:170px;left:0;right:0;color:#222}
.fdi .feature-grid{left:115px;top:232px;width:1060px;grid-template-columns:515px 545px}
.fdi .feature{font-weight:400;color:#333;font-size:13px}

.news{top:2443px;height:527px}
.news .dark-photo{background:linear-gradient(180deg,#403834 0%,#5e4638 45%,#3c4654 75%,#2b3342 100%)}
.news .sec-title{position:absolute;top:120px;left:0;right:0}
.news-item{position:absolute;top:228px;display:flex;gap:20px;width:500px}
.news-thumb{width:160px;height:160px;flex:none;border:5px solid #fff}
.news-item h3{font:700 16px "Open Sans",sans-serif;margin-bottom:4px}
.news-item p{font:600 14px/1.45 "Open Sans",sans-serif}
.news .btn{position:absolute;top:400px;left:533px}

.clients{top:2970px;height:300px}
.clients .sec-title{position:absolute;top:88px;left:0;right:0;color:#333}
.logo-row{position:absolute;top:200px;left:110px;right:110px;display:flex;justify-content:space-between;align-items:center;font:700 30px "Open Sans",sans-serif;color:#a7a9ad}
.carousel{position:absolute;top:196px;font:400 34px "Open Sans",sans-serif;color:#aaa}

.footer{top:3270px;height:275px;background:var(--blue);color:#fff}
.footer-brand{position:absolute;left:42px;top:110px;display:flex;align-items:center;gap:12px}
.footer-brand .brand-square{width:52px;height:52px}
.footer-brand .brand-name{font-size:23px}
.fcol{position:absolute;top:50px}
.fcol h4{font:700 15px "Open Sans",sans-serif;text-transform:uppercase;padding-bottom:8px;border-bottom:1px solid rgba(255,255,255,.5);margin-bottom:12px}
.fcol li{list-style:none;font:400 12.5px/1.55 "Open Sans",sans-serif}
.fcol .contact-line{display:flex;gap:8px;align-items:center;margin-top:12px;font-size:12.5px}
.newsletter{display:flex;margin-top:6px}
.newsletter span{background:#fff;color:#333;font:600 12px "Open Sans",sans-serif;padding:9px 10px;width:148px}
.newsletter b{background:#111;font:700 12px "Open Sans",sans-serif;padding:9px 14px}
.copyright{top:3545px;height:48px;background:#fff;text-align:center;font:400 11px/48px "Open Sans",sans-serif;color:#333;text-transform:uppercase}
</style>
</head>
<body>

<header class="section hero">
  <div class="hero-photo" role="img" aria-label="Cargo ship loaded with shipping containers docked at a port"></div>
  <div class="brand"><div class="brand-square"></div><div class="brand-name">RV Crestline<br>Advisory</div></div>
  <div class="topbar">
    <span><svg width="18" height="18" viewBox="0 0 24 24"><circle cx="12" cy="12" r="11" fill="none" stroke="#fff" stroke-width="2"/><path d="M8 6l2 0 1 3-1.5 1a7 7 0 0 0 4 4l1-1.5 3 1v2a1 1 0 0 1-1 1A10 10 0 0 1 7 7a1 1 0 0 1 1-1z" fill="#fff"/></svg>1 (555) 210-0147</span>
    <span><svg width="18" height="18" viewBox="0 0 24 24"><circle cx="12" cy="12" r="11" fill="none" stroke="#fff" stroke-width="2"/><rect x="6" y="8" width="12" height="8" fill="none" stroke="#fff" stroke-width="1.6"/><path d="M6 8l6 5 6-5" fill="none" stroke="#fff" stroke-width="1.6"/></svg>info@RVCrestline.example</span>
    <span class="social"><i></i><i></i><i></i></span>
  </div>
  <nav class="nav">
    <a class="active">Home</a><a>About</a><a>Our Services ▾</a><a>News</a><a>Clients</a><a>Contact</a>
  </nav>
  <div class="arrow" style="left:0"><svg width="16" height="16" viewBox="0 0 16 16"><path d="M11 2L5 8l6 6" fill="none" stroke="#fff" stroke-width="2.5"/></svg></div>
  <div class="arrow" style="right:0"><svg width="16" height="16" viewBox="0 0 16 16"><path d="M5 2l6 6-6 6" fill="none" stroke="#fff" stroke-width="2.5"/></svg></div>
  <svg class="hero-edge" width="1200" height="60" viewBox="0 0 1200 60"><polygon points="0,60 0,48 600,28 1200,0 1200,60" fill="var(--blue)"/><polygon points="0,60 0,56 600,40 1200,16 1200,60" fill="var(--grey-band)"/></svg>
</header>

<section class="section tagline">
  <h1>RV Crestline Advisory<em>is a U.S.-based international</em><strong>Consulting Firm</strong></h1>
  <p>We combined passion for success in the global business arena with hands-on experience to help foreign companies navigate the entry into U.S. markets and U.S. companies in initiating and expanding exports to foreign markets.</p>
  <a class="btn">Learn More</a>
</section>

<section class="section about">
  <div class="sec-title"><i class="mark"></i><span>About <b>RV Crestline Advisory</b></span></div>
  <p class="about-lead">Mira Talvenko has ten years of experience in economic development, foreign direct investment (FDI) and trade.</p>
  <div class="about-body">
    <p>Prior to founding RV Crestline Advisory, she worked as Director of Global Business Development – Europe at the Ozark State Development Board (OSDB) assisting European companies to expand in the state. While at the OSDB, Mira participated in a number of international trade shows and organized multiple investment and trade missions for the state’s governors.</p>
    <p>Mira was appointed by the U.S. Secretary of Commerce to the Riverbend District Export Council (RDEC), an organization of business leaders whose expertise in international business provides a source of professional advice for the region’s firms. She was elected to serve as the RDEC Vice Chair in 2017. Mira is a speaker at the Export Academy, an RDEC program providing export training and education. She will teach an International Business Management class at Riverbend State University during the fall semester of 2017.</p>
    <a class="btn">Learn More</a>
  </div>
  <div class="portrait" role="img" aria-label="Portrait photo of the company founder"></div>
</section>

<section class="section dark exports">
  <div class="dark-photo" role="img" aria-label="Container port with cranes and a city skyline at dusk"></div>
  <svg class="dark-edge" style="top:0" width="1200" height="70" viewBox="0 0 1200 70"><polygon points="0,0 1200,0 1200,8 600,40 0,14" fill="#fff"/><polygon points="0,14 600,40 1200,8 1200,16 600,50 0,26" fill="var(--blue)"/></svg>
  <div class="sec-title"><i class="mark"></i><span>RV Crestline Advisory <b>Exports</b></span></div>
  <p class="lead">We assist U.S. companies with their export initiatives by</p>
  <div class="feature-grid">
    <div class="feature"><span class="icon"><svg width="30" height="30" viewBox="0 0 30 30"><path d="M3 16l7-6 5 4 5-4 7 6-7 6-5-4-5 4z" fill="none" stroke="var(--blue)" stroke-width="2"/></svg></span>Identifying and developing new customer relationships<br>in foreign markets</div>
    <div class="feature"><span class="icon"><svg width="30" height="30" viewBox="0 0 30 30"><path d="M4 18h22l-4 7H8z M9 18v-6h12v6 M13 12V6h4v6" fill="none" stroke="var(--blue)" stroke-width="2"/></svg></span>Providing an assistance with the completion of a strategic<br>export plan</div>
    <div class="feature"><span class="icon"><svg width="30" height="30" viewBox="0 0 30 30"><path d="M4 22l8-4 4-8 6 2-3 6 8 2" fill="none" stroke="var(--blue)" stroke-width="2"/></svg></span>Organizing trade mission trips</div>
    <div class="feature"><span class="icon"><svg width="30" height="30" viewBox="0 0 30 30"><rect x="5" y="18" width="4" height="8" fill="var(--blue)"/><rect x="12" y="13" width="4" height="13" fill="var(--blue)"/><rect x="19" y="8" width="4" height="18" fill="var(--blue)"/><path d="M5 13l8-6 5 3 7-6" fill="none" stroke="var(--blue)" stroke-width="2"/></svg></span>Finding additional resources to support and grow<br>companies’ exports</div>
    <div class="feature"><span class="icon"><svg width="30" height="30" viewBox="0 0 30 30"><path d="M15 4l10 22H5z M10 16h10" fill="none" stroke="var(--blue)" stroke-width="2"/></svg></span>Coordinating successful trade show visits</div>
    <div class="feature"><span class="icon"><svg width="30" height="30" viewBox="0 0 30 30"><circle cx="15" cy="15" r="10" fill="none" stroke="var(--blue)" stroke-width="2"/><path d="M5 15h20 M15 5c-5 6-5 14 0 20 M15 5c5 6 5 14 0 20" fill="none" stroke="var(--blue)" stroke-width="1.6"/></svg></span>Connecting companies with other intern</div>
  </div>
  <svg class="dark-edge" style="bottom:0" width="1200" height="70" viewBox="0 0 1200 70"><polygon points="0,40 600,62 1200,30 1200,70 0,70" fill="#fff"/><polygon points="0,28 600,52 1200,18 1200,30 600,62 0,40" fill="var(--blue)"/></svg>
</section>

<section class="section fdi">
  <div class="sec-title"><i class="mark"></i><span>RV Crestline Advisory <b>FDI</b></span></div>
  <p class="lead">We assist international companies with navigating the entry into U.S. markets by</p>
  <div class="feature-grid">
    <div class="feature"><span class="icon"><svg width="30" height="30" viewBox="0 0 30 30"><path d="M4 9h18l4 4-2 8-6 1-3 3-5-4H5z" fill="none" stroke="#fff" stroke-width="2"/></svg></span>Managing the site selection process</div>
    <div class="feature"><span class="icon"><svg width="30" height="30" viewBox="0 0 30 30"><rect x="5" y="7" width="20" height="16" fill="none" stroke="#fff" stroke-width="2"/><path d="M9 18l5-5 3 3 5-5" fill="none" stroke="#fff" stroke-width="2"/></svg></span>Providing an appraisal of proposed incentives and financing assistance</div>
    <div class="feature"><span class="icon"><svg width="30" height="30" viewBox="0 0 30 30"><circle cx="15" cy="15" r="10" fill="none" stroke="#fff" stroke-width="2"/><path d="M15 15V5 M15 15l8 5" fill="none" stroke="#fff" stroke-width="2"/></svg></span>Collecting market data</div>
    <div class="feature"><span class="icon"><svg width="30" height="30" viewBox="0 0 30 30"><rect x="6" y="4" width="13" height="17" fill="none" stroke="#fff" stroke-width="2"/><rect x="11" y="9" width="13" height="17" fill="var(--blue)" stroke="#fff" stroke-width="2"/></svg></span>Management of the documentation process</div>
    <div class="feature"><span class="icon"><svg width="30" height="30" viewBox="0 0 30 30"><rect x="6" y="16" width="4" height="10" fill="#fff"/><rect x="13" y="10" width="4" height="16" fill="#fff"/><rect x="20" y="5" width="4" height="21" fill="#fff"/></svg></span>Site identification and analysis</div>
  </div>
</section>

<section class="section dark news">
  <div class="dark-photo" role="img" aria-label="Harbor cranes over stacked shipping containers"></div>
  <svg class="dark-edge" style="top:0" width="1200" height="70" viewBox="0 0 1200 70"><polygon points="0,0 1200,0 1200,10 600,42 0,8" fill="#fff"/><polygon points="0,8 600,42 1200,10 1200,20 600,54 0,20" fill="var(--blue)"/></svg>
  <div class="sec-title"><i class="mark"></i><span>Latest <b>News</b></span></div>
  <article class="news-item" style="left:54px">
    <div class="news-thumb" role="img" aria-label="Business colleagues talking in an office" style="background:linear-gradient(135deg,#dfe4ea,#8a9bb0)"></div>
    <div><h3>NEWS #1</h3><p>Lorem ipsum dolor sit amet, consectetuer adipiscing diam nonummy nibh euismod tincidunt ut laoreet aliquam erat volutpat. Ut wisi enim ad minim veniam, rud exerci tation ullamcorper suscipit lobortis nisl ut ea commodo consequat.</p></div>
  </article>
  <article class="news-item" style="left:626px">
    <div class="news-thumb" role="img" aria-label="City road with motion light trails in blue tones" style="background:linear-gradient(135deg,#c9d8ee,#3c5f98)"></div>
    <div><h3>NEWS #2</h3><p>Lorem ipsum dolor sit amet, consectetuer adipiscing diam nonummy nibh euismod tincidunt ut laoreet aliquam erat volutpat. Ut wisi enim ad minim veniam, rud exerci tation ullamcorper suscipit lobortis nisl ut ea commodo consequat.</p></div>
  </article>
  <a class="btn">View All News</a>
  <svg class="dark-edge" style="bottom:0" width="1200" height="80" viewBox="0 0 1200 80"><polygon points="0,50 600,76 1200,40 1200,80 0,80" fill="#fff"/><polygon points="0,36 600,64 1200,26 1200,40 600,76 0,50" fill="var(--blue)"/></svg>
</section>

<section class="section clients">
  <div class="sec-title"><i class="mark"></i><span>Our <b>Clients</b></span></div>
  <span class="carousel" style="left:116px">‹</span>
  <span class="carousel" style="right:116px">›</span>
  <div class="logo-row"><span style="margin-left:100px">Norvale</span><span>Kestrix</span><span>Altavine</span><span>Brightquill</span><span style="margin-right:100px">Solmere</span></div>
</section>

<footer class="section footer">
  <div class="footer-brand"><div class="brand-square"></div><div class="brand-name">RV Crestline<br>Advisory</div></div>
  <div class="fcol" style="left:324px;width:140px"><h4>Quick Links</h4><ul><li>Home</li><li>About Us</li><li>Our Services</li><li>News</li><li>Contact</li></ul></div>
  <div class="fcol" style="left:474px;width:190px"><h4>Services</h4><ul><li>RV Crestline Advisory – Exports</li><li>RV Crestline Advisory – FDI</li></ul></div>
  <div class="fcol" style="left:690px;width:190px"><h4>Contact</h4><ul><li>RV Crestline Advisory, LLC</li><li>Mira Talvenko, MBA</li><li>President</li></ul>
    <div class="contact-line"><svg width="18" height="18" viewBox="0 0 24 24"><circle cx="12" cy="12" r="11" fill="none" stroke="#fff" stroke-width="2"/><path d="M8 6l2 0 1 3-1.5 1a7 7 0 0 0 4 4l1-1.5 3 1v2a1 1 0 0 1-1 1A10 10 0 0 1 7 7a1 1 0 0 1 1-1z" fill="#fff"/></svg>+1 (555) 210-0147</div>
    <div class="contact-line"><svg width="18" height="18" viewBox="0 0 24 24"><circle cx="12" cy="12" r="11" fill="none" stroke="#fff" stroke-width="2"/><rect x="6" y="8" width="12" height="8" fill="none" stroke="#fff" stroke-width="1.6"/><path d="M6 8l6 5 6-5" fill="none" stroke="#fff" stroke-width="1.6"/></svg>info@RVCrestline.example</div>
  </div>
  <div class="fcol" style="left:930px;width:230px"><h4>Newsletter</h4><div class="newsletter"><span>Enter Email Address</span><b>SIGN UP</b></div></div>
</footer>

<div class="section copyright">Copyright © 2017 RV Crestline Advisory. All rights reserved.</div>

</body>
</html>
```